International Aid Org. Web Design Project

We need a new design for a non-profit/missions organization that focuses on international aid, short term missions. Our current site is www.harborwellsaid.org and it is awful We are throwing the whole thing out, so there isn't much to take. But please take a look around to get a sense of what it is that we do.

Our primary promotion comes through our director, Colin Marsh. His speaking engagements, presence on national radio and Television and book drive people to the site. Once they arrive here we want them to join our network (social network style), give to an ongoing project or research/signup for a short term missions trip (we call these pathways of kindness).

We have no strong color preferences. Not too stark, not too dark. Our logo uses Red, Black and Blue, but certainly we don't want a strictly red and blue site.

I've attached a questionnaire which is somewhat complete and may be helpful.

***PLEASE READ THIS***

On the wireframe I have a section entitiled Dad's Section. This is mislabelled. Please name that "Colin Marsh" And please include graphical buttons (not simple text links) to these 4 things:

Bio

Where Rivers Begin Again (This is the book. Please incorporate the book cover which is a file attached to the project)

Podcasts

Upcoming Events
Updates

I would like a section to the right of the slide show, listed once incorrectly as "my dad's space" with the heading "Colin Marsh".  In this section I would like 4 graphical buttons (Not text based links) to Bio, Podcasts, Upcoming Events, Where Rivers Begin Again.  I would like "Where rivers Begin Again" to incorporate the book cover, which is included in the brief.

Please also create a slide for the book utilizing some of the imagery in from the book cover.

Target Market(s)

Our audience is largely adults aged 25-60. Western speaking countries.

Industry/Entity Type

Radio

Requirements
Must have
• We need a 4 slide slide show.
Should not have
• Blue and green!

```html
<!DOCTYPE html>
<html lang="en">
<head>
<meta charset="utf-8">
<title>Harborwell Aid</title>
<link href="https://fonts.googleapis.com/css2?family=Arimo:wght@400;700&display=swap" rel="stylesheet">
<style>
  :root {
    --red: #c8202f;
    --ink: #1f1f1f;
    --bar: #1c1c1c;
    --bar-top: #2e2e2e;
    --text: #2a2a2a;
    --muted: #7a7a7a;
    --line: #d4d4d4;
    --page-low: #c9c9c9;
    --rule: #bdbdbd;
  }
  * { box-sizing: border-box; margin: 0; padding: 0; }
  html, body { width: 1200px; height: 960px; overflow: hidden; }
  body {
    font-family: "Arimo", Arial, sans-serif;
    color: var(--text);
    background: linear-gradient(180deg, #fff 0, #fff 500px, #e6e6e6 620px, var(--page-low) 889px);
    position: relative;
  }
  .top-rule { position: absolute; left: 0; top: 0; width: 1200px; height: 7px; background: var(--rule); }

  .brand { position: absolute; left: 98px; top: 58px; display: flex; align-items: center; gap: 12px; }
  .brand-mark { width: 22px; height: 22px; background: var(--red); }
  .brand-name { font-size: 32px; font-weight: 700; color: var(--ink); line-height: 1; }

  .main-nav {
    position: absolute; left: 77px; top: 139px; width: 1046px; height: 51px;
    background: linear-gradient(180deg, var(--bar-top), var(--bar));
    border-bottom: 4px solid var(--red);
  }
  .main-nav a {
    position: absolute; top: 0; height: 47px; line-height: 47px;
    color: #fff; font-size: 15px; font-weight: 700; text-decoration: none; white-space: nowrap;
  }
  .main-nav a.active { background: var(--red); left: 0; width: 84px; text-align: center; }
  .search {
    position: absolute; left: 801px; top: 9px; width: 238px; height: 30px;
    background: #fff; border-radius: 2px; font-size: 14px; color: #999;
    padding: 0 12px; line-height: 30px;
  }
  .search svg { position: absolute; right: 10px; top: 8px; }

  .hero {
    position: absolute; left: 77px; top: 202px; width: 742px; height: 290px;
    background: linear-gradient(180deg, #aebcc8 0%, #d4dce3 45%, #e9ecee 100%);
  }

  .quick-links { position: absolute; left: 839px; top: 202px; width: 286px; }
  .quick-links h2 {
    height: 59px; background: var(--red); color: #fff;
    font-size: 33px; font-weight: 400; line-height: 59px; padding-left: 18px; position: relative;
  }
  .quick-links a {
    display: block; position: relative; height: 56px; margin-top: 2px;
    background: linear-gradient(180deg, #2c2c2c, #161616);
    color: #fff; font-size: 24px; line-height: 56px; padding-left: 20px; text-decoration: none;
  }
  .quick-links svg { position: absolute; right: 16px; top: 50%; transform: translateY(-50%); }

  .column-title {
    position: absolute; top: 526px; font-size: 21px; font-weight: 400; color: var(--ink);
  }
  .card {
    position: absolute; top: 565px; width: 329px; height: 250px; background: #fff;
    border: 1px solid var(--line); box-shadow: 3px 4px 6px rgba(0,0,0,.18);
    padding: 15px 16px; font-size: 12.5px; line-height: 17px; color: var(--muted);
  }
  .photo { display: block; width: 295px; height: 102px; background: linear-gradient(135deg, #8a7f62, #c9c4b4 55%, #6e8a5a); }
  .card .photo.bottom { margin-top: 18px; }
  .card .photo.top { margin-bottom: 7px; }
  .news-item { padding: 0 14px; margin-bottom: 24px; }
  .news-item h3 { font-size: 13px; font-weight: 700; color: #555; margin-bottom: 6px; }
  .read-more {
    position: absolute; top: 832px; font-size: 13px; font-weight: 700; color: var(--ink); text-decoration: none;
  }

  .site-footer {
    position: absolute; left: 0; top: 889px; width: 1200px; height: 71px; background: var(--bar);
    color: #ddd; font-size: 12px;
  }
  .footer-links { position: absolute; left: 80px; top: 22px; }
  .footer-links a { color: #ddd; text-decoration: none; }
  .footer-links span { margin: 0 7px; }
  .copyright { position: absolute; right: 91px; top: 22px; }
</style>
</head>
<body>
  <div class="top-rule"></div>

  <header class="brand">
    <span class="brand-mark"></span>
    <span class="brand-name">Harborwell Aid</span>
  </header>

  <nav class="main-nav">
    <a class="active" href="#">HOME</a>
    <a href="#" style="left:98px">ABOUT US</a>
    <a href="#" style="left:211px">PROJECTS</a>
    <a href="#" style="left:329px">JOURNEYS</a>
    <a href="#" style="left:446px">MY HARBORWELL AID</a>
    <a href="#" style="left:634px">CONTACT US</a>
    <div class="search">Search
      <svg width="14" height="14" viewBox="0 0 14 14"><circle cx="6" cy="6" r="4.5" fill="none" stroke="#777" stroke-width="1.6"/><line x1="9.3" y1="9.3" x2="13" y2="13" stroke="#777" stroke-width="1.8"/></svg>
    </div>
  </nav>

  <div class="hero" role="img" aria-label="Slide photo: young people jumping with colourful umbrellas against a pale sky"></div>

  <aside class="quick-links">
    <h2>Quick links
      <svg width="36" height="36" viewBox="0 0 36 36"><g fill="none" stroke="#fff" stroke-width="4"><rect x="4" y="13" width="17" height="10" rx="5" transform="rotate(40 12 18)"/><rect x="15" y="13" width="17" height="10" rx="5" transform="rotate(40 24 18)"/></g></svg>
    </h2>
    <a href="#">Buy the Book
      <svg width="30" height="34" viewBox="0 0 30 34"><path d="M2 2h22a4 4 0 0 1 4 4v26H6a4 4 0 0 1-4-4z" fill="#fff"/><path d="M9 2v12l3-3 3 3V2" fill="#222"/></svg>
    </a>
    <a href="#">Podcasts
      <svg width="32" height="38" viewBox="0 0 32 38"><g fill="none" stroke="#fff" stroke-width="3"><path d="M6 24a13 13 0 1 1 20 0"/><path d="M11 20a7 7 0 1 1 10 0"/></g><circle cx="16" cy="15" r="3" fill="#fff"/><path d="M13 22h6l-1 14h-4z" fill="#fff"/></svg>
    </a>
    <a href="#">Upcoming events
      <svg width="32" height="32" viewBox="0 0 32 32"><rect x="2" y="5" width="28" height="25" rx="2" fill="#fff"/><rect x="8" y="1" width="3" height="7" fill="#fff"/><rect x="21" y="1" width="3" height="7" fill="#fff"/><g fill="#222"><rect x="6" y="12" width="4" height="4"/><rect x="12" y="12" width="4" height="4"/><rect x="18" y="12" width="4" height="4"/><rect x="24" y="12" width="3" height="4"/><rect x="6" y="19" width="4" height="4"/><rect x="12" y="19" width="4" height="4"/><rect x="18" y="19" width="4" height="4"/><rect x="24" y="19" width="3" height="4"/></g></svg>
    </a>
    <a href="#">Bio
      <svg width="34" height="32" viewBox="0 0 34 32"><circle cx="17" cy="9" r="8" fill="#fff"/><path d="M1 32c0-10 7-14 16-14s16 4 16 14z" fill="#fff"/></svg>
    </a>
  </aside>

  <h2 class="column-title" style="left:86px">PROJECTS OVERVIEW</h2>
  <h2 class="column-title" style="left:440px">LATEST NEWS HEADLINES</h2>
  <h2 class="column-title" style="left:808px">JOURNEYS</h2>

  <section class="card" style="left:77px">
    <p>Lorem ipsum dolor sit amet, consectetuer adipiscing elit. Aenean commodoLorem ipsum dolor sit amet, consectetuer adipiscing elit. Aenean commodoLorem ipsum dolor sit amet, csectetuer adipiscing elit. Aenean commodoLorem ipsum dolor sit amet,</p>
    <div class="photo bottom" role="img" aria-label="Photo: volunteers outdoors in front of a house"></div>
  </section>

  <section class="card" style="left:438px;padding-top:14px">
    <div class="news-item"><h3>Lorem ipsum dolor sit amet,</h3><p>Lorem ipsum dolor sit amet, consectetuer adipiscing elit. Aenean commodo</p></div>
    <div class="news-item"><h3>Lorem ipsum dolor sit amet,</h3><p>Lorem ipsum dolor sit amet, consectetuer adipiscing elit. Aenean commodo</p></div>
    <div class="news-item"><h3>Lorem ipsum dolor sit amet,</h3><p>Lorem ipsum dolor sit amet, consectetuer adipiscing elit. Aenean commodo</p></div>
  </section>

  <section class="card" style="left:796px">
    <div class="photo top" role="img" aria-label="Photo: volunteers outdoors in front of a house"></div>
    <p>Lorem ipsum dolor sit amet, consectetuer adipiscing elit. Aenean commodoLorem ipsum dolor sit amet, consectetuer adipiscing elit. Aenean commodoLorem ipsum dolor sit amet, consectetuer adipiscing elit. Aenean commodoLorem ipsum dolor sit amet,</p>
  </section>

  <a class="read-more" href="#" style="left:303px">[ Read more ]</a>
  <a class="read-more" href="#" style="left:663px">[ Read more ]</a>
  <a class="read-more" href="#" style="left:1024px">[ Read more ]</a>

  <footer class="site-footer">
    <div class="footer-links">
      <a href="#">HOME</a><span>|</span><a href="#">ABOUT US</a><span>|</span><a href="#">PROJECTS</a><span>|</span><a href="#">JOURNEYS</a><span>|</span><a href="#">MY HARBORWELL AID</a><span>|</span><a href="#">CONTACT US</a>
    </div>
    <div class="copyright">© 2012 &nbsp;Harborwell Aid</div>
  </footer>
</body>
</html>
```